Anzeigengestaltung für Bernstein Ankaufstage in Wien
Zielgruppe
Zweck dieser Anzeige ist:
sowiele Leute wie möglich zu überzeugen, mit Ihrem Bernstein, zu uns in die Ankaufsaktion zu kommen.
Wer wir sind:
Wir sind eine Firma aus Deutschland, die sich auf die Bewertung und den Ankauf von Bernstein (Rohbernstein, Bernsteinschmuck, Kunstobjekte aus Bernstein etc. ) spezialisiert hat.
Wir führen in verschiedenen Städten Aktionen durch, in denen wir Bernstein bewerten und ggf. auch ankaufen.
Zielgruppe:
Alle leser einer Tageszeitung, Alter 50 + überwiegend ältere Damen, und generel Haushalte die Bernstein besitzen
siehe Bsp. Anzeige Wien (Datei upload)
Aufgabenstellung
Anzeigengröße B 198 mm x H 270 mm
Technische Angaben siehe PDF Tageszeitungproduktion (Datei upload)
Wir wollen auf jedenfall eine Anzeige die auch effektreich ist, nicht nur 2-dimensional und platt bleibt, sondern auch verschiedene Tiefen hat. Aber sie soll trotzdem plakativ sein.
Die Anzeige muss Seriös, Auffälig, gut lesbar, edel, frisch,..... AKTION!!
Zielgruppe ansprechen
Direkt erkennbar sein was die Anzeige bezwecken soll
Unser Hauptinteresse liegt auf den gelben ketten, davon haben wir auch 2 Bilder beigefügt.
Das wichtigste Bild ist Bild: "bernstein_2.jpg", dieses sollte schon irgendwo groß auftauchen.
Das soll auf die Anzeige:
- Textteil wie Beispielsdatei.
- AKTION
- Was....Bernstein Ankaufs-Tage in Wien
- Bernstein-Wertschätzung und Ankauf in Wien
- Wann.....vom 03.08.2017-05.08.2017
- Uhrzeit von 10:00 Uhr bis 17:00 Uhr
- Wo.... Hotel Ostara Palais, Lindauer Gasse 14, 1010 Wien, Raum: Salon 3
- Was Kaufen Wir....... Bernsteinschmuck, Bernsteinketten, Bernsteinobjekte, Rohbernsteine ab 10 g,
Bernstein Kunstgegenstände.
- Wir bieten Ihnen eine kostenlose Wertschätzung Ihrer Bernsteinstücke sowie einen
Bar-Ankauf vor Ort.
- Unser Logo
- Unsere Website www.lindwerk-handel.de
- rechts oben in der Anzeige muss das Wort -ANZEIGE- in klein stehen.
Vermerk, Achtung !!! wir kaufen nur unbehandelten Naturbernstein!!!!
siehe Bsp. Anzeige Wien bei (Datei upload)

```html
<!DOCTYPE html>
<html lang="de">
<head>
<meta charset="utf-8">
<title>Vergessene Schätze – Anzeige</title>
<link href="https://fonts.googleapis.com/css2?family=Montserrat:wght@300;400;600;700;800&display=swap" rel="stylesheet">
<style>
  :root {
    --backdrop: #e6e6e7;
    --paper: #ffffff;
    --ink: #1f1f1f;
    --body-ink: #4a4a4a;
    --muted: #9a9a9a;
    --amber: #eda221;
    --amber-deep: #d9781a;
    --amber-light: #f7c54a;
    --raw-brown: #8a5a2a;
  }
  * { box-sizing: border-box; margin: 0; padding: 0; }
  html, body {
    width: 1200px; height: 898px; overflow: hidden;
    background: var(--backdrop);
    font-family: "Montserrat", sans-serif;
  }
  .ad-page {
    position: absolute; left: 285px; top: 19px;
    width: 630px; height: 860px;
    background: var(--paper);
    color: var(--ink);
  }
  .ad-label {
    position: absolute; right: 44px; top: 34px;
    font-size: 7px; letter-spacing: .04em; color: var(--muted);
  }
  .headline {
    position: absolute; left: 40px; top: 112px;
    font-size: 40px; line-height: 1.02; letter-spacing: .01em;
  }
  .headline .thin { font-weight: 300; display: block; }
  .headline .bold { font-weight: 800; display: block; }
  .necklace-photo {
    position: absolute; left: 335px; top: 70px;
    width: 255px; height: 180px; border-radius: 48% 50% 45% 52%;
    background: radial-gradient(ellipse at 45% 60%, var(--amber-light) 0%, var(--amber) 45%, var(--amber-deep) 80%, rgba(217,120,26,0) 100%);
  }
  .intro {
    position: absolute; left: 40px; top: 215px; width: 280px;
    font-size: 10px; font-weight: 700; line-height: 1.5;
  }
  .columns {
    position: absolute; left: 40px; top: 335px; width: 555px;
    display: grid; grid-template-columns: repeat(3, 1fr); column-gap: 15px;
  }
  .column {
    font-size: 7.4px; font-weight: 300; line-height: 1.45; color: var(--body-ink);
  }
  .column h3 {
    font-size: 8px; font-weight: 700; color: var(--ink); margin: 12px 0 2px;
  }
  .raw-amber-photo {
    margin-top: 12px; width: 150px; height: 60px; border-radius: 40% 45% 35% 40%;
    background: linear-gradient(100deg, var(--raw-brown) 0%, #b8782e 45%, var(--amber) 100%);
  }
  .brand {
    margin-top: 20px; display: flex; align-items: center; justify-content: flex-end; gap: 6px;
  }
  .brand-dot { width: 20px; height: 20px; border-radius: 50%; background: var(--amber); }
  .brand-name { font-size: 11px; font-weight: 600; color: var(--ink); letter-spacing: .03em; }
  .offer-title {
    position: absolute; left: 40px; top: 660px;
    font-size: 18px; font-weight: 700; line-height: 1.25; color: var(--amber);
  }
  .offer-text {
    position: absolute; left: 40px; top: 722px; width: 200px;
    font-size: 9.5px; font-weight: 700; line-height: 1.55;
  }
  .info-block {
    position: absolute; font-size: 8.5px; font-weight: 300; line-height: 1.6; color: var(--body-ink);
  }
  .info-block h4 { font-size: 8.5px; font-weight: 700; color: var(--amber); }
  .purchase-list { left: 265px; top: 680px; width: 150px; }
  .venue { left: 430px; top: 660px; width: 170px; }
  .contact { margin-top: 8px; }
  .contact .web { color: var(--amber); font-weight: 600; }
</style>
</head>
<body>
  <main class="ad-page">
    <div class="ad-label">ANZEIGE</div>

    <h1 class="headline"><span class="thin">VERGESSENE</span><span class="bold">SCHÄTZE</span></h1>

    <div class="necklace-photo" role="img" aria-label="Foto: gelbe und orangefarbene Bernsteinkette"></div>

    <p class="intro">Einst als kostbare Fracht entlang der Bernsteinstraße (östliche römische Route) gelangte Bernstein von der Nord- und Ostsee nach Süden in den Mittelmeerraum. Gezeichnet durch kunstvoll gefertigte Gegenstände und allerlei Schmuck rühmt sich das fossile Harz einer langen und vielfältigen Geschichte.</p>

    <div class="columns">
      <section class="column">
        <p>Doch diese facettenreiche Geschichte scheint heute für die meisten in Vergessenheit geraten zu sein und klingt bestenfalls noch wie ein Märchen aus der Kindheit. Oft sogar als „langweilig“ oder „aus der Mode gekommen“ gebrandmarkt, wurde der Naturbernstein hier zunehmend von Juwelier-Schaufenstern und Vitrinen verbannt.</p>
        <div class="raw-amber-photo" role="img" aria-label="Foto: Rohbernsteinstücke"></div>
        <h3>Ein neues Kapitel</h3>
        <p>Nichtsdestoweniger wird dem Bernstein heute weltweit mehr Wertschätzung gezollt als je zuvor. Seit Neuestem wurde ein neues Kapitel aufgeschlagen. Die Bernsteinstraße, die einst gen Süden ging, führt heute bis nach China im Fernen Osten. Die aktuelle Nachfrage aus Asien hat</p>
      </section>

      <section class="column">
        <p>den Handel mit Bernstein auf ganz neue Weise wiederbelebt und den Preis teilweise beträchtlich ansteigen lassen. Was mitunter in Wiener Haushalten seit Jahrzehnten in Schmuckkästchen verstaubt, wird in China als begehrtes Schmuckstück teuer gehandelt. Dort gilt Bernstein unter anderem als Symbol des Reichtums und wird stolz in der Öffentlichkeit getragen.</p>
        <h3>Große Werte</h3>
        <p>Die Wertbestimmung für Bernstein hat sich jedoch gewandelt und abhängig von bestimmten Merkmalen variiert der Preis sehr stark. Der hier sonst sehr übliche cognacfarbene und transparente Bernsteinschmuck ist kaum mehr gefragt und in jeglicher Form behandelter oder gepresster Bernstein findet so gut wie keine Beachtung mehr. Dahingegen dominiert heute vor allem der un-</p>
      </section>

      <section class="column">
        <p>behandelte naturbelassene Honigbernstein den Handel. Gelb bis orangefarbene milchige in Oliven- oder Kugelform gefertigte Ketten sind die absoluten Renner. Antike Bernsteinketten, die durch Verwitterung im Laufe der Jahre unterschiedlich stark rot bis rotbraun gefärbt wurden, sind besonders interessant. Auch sonstige Schmuckstücke, wie etwa Armbänder, Anhänger, Ringe, Broschen und andere Kleingegenstände sind beliebt. Das gilt auch für Schmuckschatullen, Schnitzereien und Kunstgegenstände aus Natur-Bernstein. Zum einen ist natürlich das Alter und der Zustand für den Preis entscheidend, aber auch Dinge wie Farbe, Größe und Marmorierung sind wichtige Faktoren. Sammler bevorzugen überwiegend gut erhaltene und antike Stücke. Es empfiehlt sich in jedem Fall einen geeigneten Fachmann zu Rate zu ziehen.</p>
        <div class="brand"><span class="brand-dot"></span><span class="brand-name">LINDWERK HANDEL</span></div>
      </section>
    </div>

    <h2 class="offer-title">Bernstein-Wertschätzung<br>und Ankauf in Wien</h2>
    <p class="offer-text">Wir bieten Ihnen eine kostenlose Wertschätzung Ihrer Bernsteinstücke sowie einen Bar-Ankauf vor Ort.</p>

    <div class="info-block purchase-list">
      <h4>Wir kaufen</h4>
      <p>Bernsteinschmuck, Bernsteinketten, Rohbernsteine ab 10g und Kunstgegenstände aus Bernstein.</p>
    </div>

    <div class="info-block venue">
      <h4>Hotel Ostara Palais</h4>
      <p>03. bis 05.08.2017, 10.00 bis 17.00<br>Lindauer Gasse 14, 1010 Wien<br>Raum: Salon 3</p>
      <p class="contact">Tel. +43 660 5128 3307<br><span class="web">www.lindwerk-handel.de</span></p>
    </div>
  </main>
</body>
</html>
```